Ridge Fitness & Training Design

See photo attached
Obviously I want that second logo attached to it.
Ridge Fitness & Training instead of the old one.
I had business cards already but I want to go back to a more professional look.
Open the some ideas but I would love around the same look that is shown on the photos. Easy money I would say for a designer

Target Market(s)

Fitness

Industry/Entity Type

Business

Contact Information for Business Card

Maxime Delorne
Director, Strength & Conditioning Head Coach
148 Carrow Street - Melbourne, Australia VIC 3000
0461092436
ABN 83104629578
mdelorne@ridgefitnessandtraining.com
www.ridgefitnessandtraining.com
facebook.com/ridgefitnessandtraining.com

Requirements
Must have
• Look Professional same or similar to uploaded photos.
• open to creativity
• black colour

```html
<!DOCTYPE html>
<html lang="en">
<head>
<meta charset="utf-8">
<title>Ridge Fitness &amp; Training – Business Card</title>
<link rel="stylesheet" href="https://fonts.googleapis.com/css2?family=Questrial&family=Open+Sans:wght@400&display=swap">
<style>
  :root {
    --page: #d6d6d6;
    --card: #050505;
    --white: #ffffff;
    --red: #e0382b;
    --muted: #e6e6e6;
  }
  * { margin: 0; padding: 0; box-sizing: border-box; }
  html, body {
    width: 1200px;
    height: 1000px;
    overflow: hidden;
    background: var(--page);
  }
  .sheet {
    position: relative;
    width: 1200px;
    height: 1000px;
  }
  .card {
    position: absolute;
    left: 250px;
    width: 700px;
    height: 400px;
    background: var(--card);
    color: var(--white);
    box-shadow: 0 8px 22px rgba(0,0,0,0.25);
  }
  .card--front { top: 60px; }
  .card--back { top: 530px; }

  .brand-name {
    font-family: "Questrial", sans-serif;
    font-weight: 400;
    color: var(--white);
    text-transform: uppercase;
    letter-spacing: 1px;
    line-height: 1.05;
  }
  .brand-mark {
    display: inline-block;
    background: var(--red);
    flex: none;
  }

  /* Front */
  .front-lockup {
    position: absolute;
    left: 60px;
    top: 70px;
    display: flex;
    align-items: center;
    gap: 22px;
  }
  .front-lockup .brand-mark { width: 58px; height: 58px; }
  .front-lockup .brand-name { font-size: 38px; }

  /* Back */
  .back-lockup {
    position: absolute;
    left: 45px;
    top: 150px;
    width: 250px;
    display: flex;
    align-items: center;
    gap: 16px;
  }
  .back-lockup .brand-mark { width: 40px; height: 40px; }
  .back-lockup .brand-name { font-size: 24px; }

  .divider {
    position: absolute;
    left: 322px;
    top: 38px;
    width: 6px;
    height: 330px;
    background: var(--white);
  }
  .contact {
    position: absolute;
    left: 356px;
    top: 48px;
    width: 320px;
  }
  .contact .brand-name {
    font-size: 27px;
    margin-bottom: 14px;
  }
  .contact-list {
    list-style: none;
    font-family: "Open Sans", sans-serif;
    font-size: 12.5px;
    line-height: 1.7;
    color: var(--muted);
  }
  .contact-list .gap { margin-top: 8px; }
</style>
</head>
<body>
  <main class="sheet">
    <section class="card card--front" aria-label="Business card front">
      <div class="front-lockup">
        <span class="brand-mark" aria-hidden="true"></span>
        <h1 class="brand-name">Ridge Fitness<br>&amp; Training</h1>
      </div>
    </section>

    <section class="card card--back" aria-label="Business card back">
      <div class="back-lockup">
        <span class="brand-mark" aria-hidden="true"></span>
        <p class="brand-name">Ridge Fitness<br>&amp; Training</p>
      </div>
      <div class="divider" aria-hidden="true"></div>
      <div class="contact">
        <h2 class="brand-name">Ridge Fitness<br>&amp; Training</h2>
        <ul class="contact-list">
          <li>Maxime Delorne Director, Strength &amp; Conditioning Head</li>
          <li>Coach 148 Carrow Street - Melbourne, Australia</li>
          <li>VIC 3000 0461092436</li>
          <li>ABN 83104629578</li>
          <li class="gap">mdelorne@ridgefitnessandtraining.com</li>
          <li>www.ridgefitnessandtraining.com</li>
          <li>facebook.com/ridgefitnessandtraining.com</li>
        </ul>
      </div>
    </section>
  </main>
</body>
</html>
```